Brightfernrx website

We are a weight loss clinic and we need a website built. please look at these websites for content and style. Just need like 5 pages see samples. AI files of logo are not avail yet so use sample for place set

https://glowshiftstudio.com/
ortanvital.com
https://pinecrestclinicalbodybalance.com/
https://yourslimmingnook.com/
https://qrvskinstudio.com/treatments/weight-loss-injections/

Target Market(s)

Women

Industry/Entity Type

weight loss

Coding

Coded - Design and coding required

Number of Pages Required

5+ page

Requirements
Nice to have
• please make look like a medspa website

```html
<!DOCTYPE html>
<html lang="en">
<head>
<meta charset="utf-8">
<title>Brightfernrx – Weight Loss Clinic</title>
<link rel="stylesheet" href="https://fonts.googleapis.com/css2?family=Poppins:wght@400;500;600;700&family=Mr+Dafoe&display=swap">
<style>
:root{
  --green:#0fa382;
  --green-soft:#35b99b;
  --ink:#141414;
  --muted:#3a3a3a;
  --paper:#f4f4f2;
  --white:#ffffff;
  --star:#f2c218;
  --script:"Mr Dafoe", cursive;
}
*{box-sizing:border-box;margin:0;padding:0}
html,body{width:1200px;height:5357px;overflow:hidden}
body{position:relative;font-family:"Poppins",sans-serif;color:var(--ink);background:var(--white)}
section,header,footer{position:absolute;left:0;width:1200px}
.abs{position:absolute}
.brand{font-weight:600;font-size:21px;color:var(--ink);display:flex;align-items:center;gap:8px}
.brand-dot{width:12px;height:12px;border-radius:50%;background:var(--green)}
.btn{position:absolute;background:var(--green);color:var(--white);border-radius:30px;display:flex;align-items:center;justify-content:center;font-size:14px;font-weight:500}
.center{text-align:center;left:0;width:1200px}
.h2{font-weight:600;font-size:30px}
.lead{font-size:14px;line-height:21px;color:var(--muted)}
.ph{position:absolute}

/* hero */
.hero{top:0;height:760px;background:var(--paper)}
.nav{top:34px;left:500px;display:flex;gap:42px;font-size:15px}
.eyebrow{left:125px;top:196px;font-size:14px;display:flex;gap:8px;align-items:center}
.hero-title{left:120px;top:226px;font-size:70px;font-weight:600;line-height:76px}
.hero-title .script{font-family:var(--script);color:var(--green);font-weight:400;font-size:84px}
.hero-copy{left:120px;top:416px;width:385px;font-size:13.5px;line-height:21px}
.ring{left:567px;top:166px;width:500px;height:500px;border-radius:50%;background:var(--white)}
.portrait{left:619px;top:218px;width:396px;height:396px;border-radius:50%;background:radial-gradient(circle at 50% 40%,#9fdccd,var(--green) 70%)}
.stat-card{left:562px;top:162px;width:108px;height:108px;border-radius:16px;background:var(--white);box-shadow:0 4px 14px rgba(0,0,0,.08);text-align:center}
.achieve{left:582px;top:641px;width:236px;height:62px;border-radius:14px;background:var(--white);box-shadow:0 4px 14px rgba(0,0,0,.08);display:flex;align-items:center;gap:18px;padding:0 12px;font-size:14px}
.achieve-icon{width:42px;height:42px;border-radius:10px;background:var(--green);display:flex;align-items:center;justify-content:center}
.star-dot{width:58px;height:58px;border-radius:50%;background:var(--white);box-shadow:0 4px 12px rgba(0,0,0,.08);display:flex;align-items:center;justify-content:center}

/* why */
.why{top:900px;height:700px}
.band{left:125px;top:296px;width:950px;height:302px;border-radius:48px;background:var(--green)}
.card{top:185px;width:250px;height:381px;background:var(--white);border-radius:30px;box-shadow:0 0 0 10px rgba(255,255,255,.55),0 6px 20px rgba(0,0,0,.06);text-align:center}
.card .photo{position:absolute;left:16px;top:17px;width:218px;height:171px;border-radius:22px}
.stars{color:var(--star);letter-spacing:2px;font-size:16px}
.card .stars{position:absolute;top:184px;left:55px;width:140px;background:var(--white);border-radius:12px;font-size:14px}
.card h3{position:absolute;top:233px;width:100%;font-size:18px;font-weight:500}
.card p{position:absolute;top:270px;left:30px;width:190px;font-size:10.5px;line-height:17px}

/* benefits */
.benefits{top:1600px;height:650px}
.benefits h2{left:657px;top:168px;font-size:31px;font-weight:600;line-height:38px}
.benefits h2 span{color:var(--green)}
.benefits .copy{left:657px;top:262px;width:385px;font-size:14px;line-height:20px}
.benefits ul{left:657px;top:373px;list-style:none;font-size:14px}
.benefits li{display:flex;gap:14px;align-items:center;height:31.5px}

/* testimonial */
.review{top:2357px;height:478px;background:var(--paper)}
.review .stars{font-size:36px;letter-spacing:6px}
.quote{left:205px;top:173px;width:790px;font-size:13.5px;line-height:26px;text-align:center}

/* care */
.care{top:2950px;height:850px}
.h2 .script{font-family:var(--script);color:var(--green);font-weight:400;font-size:26px}
.care-card{top:222px;width:458px;height:578px;background:#f7f6f3}
.care-card .photo{position:absolute;left:31px;top:31px;width:396px;height:275px;border-radius:8px}
.care-card h3{position:absolute;left:31px;top:328px;width:400px;font-size:24px;font-weight:500;line-height:33px}
.care-card h3 span{color:var(--green)}
.care-card p{position:absolute;left:31px;top:434px;width:396px;font-size:13px;line-height:26px}

/* team */
.team{top:3900px;height:550px}
.member{top:193px;width:220px;text-align:center}
.member .avatar{margin:0 auto;width:204px;height:204px;border-radius:50%;border:2px solid var(--green-soft);background:radial-gradient(circle at 50% 40%,#f3ede6,#d9d4cf)}
.member h4{margin-top:28px;font-size:14px;font-weight:600}
.member span{font-family:var(--script);color:var(--green);font-size:15px}

/* newsletter */
.news{top:4613px;left:125px;width:950px;height:244px;border-radius:60px;background:var(--green-soft);color:var(--white)}
.news h2{left:62px;top:36px;font-size:32px;font-weight:500}
.news p{left:62px;top:77px;width:440px;font-size:13.5px;line-height:21px}
.field{left:62px;top:158px;width:414px;height:46px;border-radius:8px;background:rgba(255,255,255,.22);font-size:14px;padding-left:24px;display:flex;align-items:center}
.field .sub{position:absolute;right:8px;top:7px;width:112px;height:32px;border-radius:6px;background:var(--white);color:var(--green);display:flex;align-items:center;justify-content:center}

/* footer */
.footer{top:5017px;height:340px;background:var(--paper)}
.foot-links{font-size:13px;line-height:32px}
.rule{left:120px;top:260px;width:960px;height:1px;background:#d9d9d6}
</style>
</head>
<body>

<section class="hero">
  <div class="abs brand" style="left:112px;top:26px"><span class="brand-dot"></span>Brightfernrx</div>
  <nav class="abs nav"><span>Home</span><span>Surgery</span><span>Doctors</span><span>Blog</span><span>Contact Us</span></nav>
  <div class="btn" style="left:971px;top:29px;width:102px;height:34px;font-size:12px">Get Started</div>

  <div class="abs eyebrow">
    <svg width="16" height="16" viewBox="0 0 16 16"><path d="M8 0L9.5 6.5 16 8 9.5 9.5 8 16 6.5 9.5 0 8 6.5 6.5Z" fill="var(--green)"/></svg>
    Welcome to our clinic
  </div>
  <h1 class="abs hero-title"><span class="script">Weight</span> Loss<br>Clinic</h1>
  <p class="abs hero-copy">If you are frustrated by diets that don’t work, we can help. Our medically supervised weight loss plans are designed to help you lose fat and feel healthier. We combine proven medical treatments to help you lose weight in a structured plan that is easy to stick with.</p>
  <div class="btn" style="left:121px;top:563px;width:147px;height:44px">Learn More</div>

  <div class="abs ring"></div>
  <div class="ph portrait" role="img" aria-label="Smiling woman in a teal tank top giving a thumbs up with a measuring tape around her waist"></div>
  <div class="abs stat-card">
    <svg class="abs" style="left:19px;top:12px" width="70" height="70" viewBox="0 0 70 70"><circle cx="35" cy="35" r="28" fill="none" stroke="#e3e3e3" stroke-width="8"/><path d="M7 35A28 28 0 0 1 63 35" fill="none" stroke="var(--green)" stroke-width="8"/></svg>
    <div class="abs" style="top:37px;width:108px;font-size:11px;font-weight:600">100%</div>
    <div class="abs" style="top:69px;width:108px;font-size:7px">Weight loss</div>
    <div class="abs" style="top:78px;width:108px;font-size:14px;font-weight:600">Ideal</div>
  </div>
  <div class="abs achieve">
    <div class="achieve-icon"><svg width="22" height="22" viewBox="0 0 16 16"><path d="M8 0L9.5 6.5 16 8 9.5 9.5 8 16 6.5 9.5 0 8 6.5 6.5Z" fill="#fff"/></svg></div>
    Achievement Unlock
  </div>
  <div class="abs star-dot" style="left:951px;top:225px"><svg width="22" height="22" viewBox="0 0 24 24"><path d="M12 2l3 7 7 .6-5.4 4.7 1.7 7.3L12 17.8 5.7 21.6l1.7-7.3L2 9.6 9 9z" fill="var(--green)"/></svg></div>
  <div class="abs star-dot" style="left:969px;top:675px"><svg width="22" height="22" viewBox="0 0 24 24"><path d="M12 2l3 7 7 .6-5.4 4.7 1.7 7.3L12 17.8 5.7 21.6l1.7-7.3L2 9.6 9 9z" fill="var(--green)"/></svg></div>
</section>

<section class="why">
  <h2 class="abs center h2" style="top:53px">WHY US?</h2>
  <p class="abs center lead" style="top:104px;left:210px;width:780px">If you are frustrated by diets that don’t work, we can help. Our medically supervised weight loss plans are designed to help you lose fat and feel healthier. We combine proven medical</p>
  <div class="abs band"></div>
  <article class="abs card" style="left:179px">
    <div class="ph photo" role="img" aria-label="Doctor in a white coat holding a stethoscope" style="background:linear-gradient(135deg,#eef0f2,#b8c3cc)"></div>
    <div class="stars">★★★★★</div>
    <h3>MEDICAL EXPERTS</h3>
    <p>If you are frustrated by diets that don’t work, we can help. Our medically supervised weight loss plans are designed to help you</p>
  </article>
  <article class="abs card" style="left:468px">
    <div class="ph photo" role="img" aria-label="Lab technician working with modern laboratory equipment" style="background:linear-gradient(135deg,#c9d6e2,#4f5f73)"></div>
    <div class="stars">★★★★★</div>
    <h3>LATEST TECHNOLOGY</h3>
    <p>If you are frustrated by diets that don’t work, we can help. Our medically supervised weight loss plans are designed to help you</p>
  </article>
  <article class="abs card" style="left:755px">
    <div class="ph photo" role="img" aria-label="Group fitness class training in a gym" style="background:linear-gradient(135deg,#5a4a40,#1f1a18)"></div>
    <div class="stars">★★★★★</div>
    <h3>DISCOVER NEW</h3>
    <p>If you are frustrated by diets that don’t work, we can help. Our medically supervised weight loss plans are designed to help you</p>
  </article>
</section>

<section class="benefits">
  <div class="ph" role="img" aria-label="Patient being assisted by a nurse during a medical scan" style="left:123px;top:93px;width:470px;height:468px;border-radius:14px;background:linear-gradient(135deg,#d9d6d0,#8a8f96 55%,#4b5560)"></div>
  <h2 class="abs"><span>BENIFITS</span> OF OUR<br>PROGRAM</h2>
  <p class="abs copy">If you are frustrated by diets that don’t work, we can help. Our medically supervised weight loss plans are designed to help you lose fat and feel healthier. We combine proven medical</p>
  <ul class="abs">
    <li><svg width="16" height="16" viewBox="0 0 16 16"><path d="M8 0L9.5 6.5 16 8 9.5 9.5 8 16 6.5 9.5 0 8 6.5 6.5Z" fill="var(--green)"/></svg>If you are frustrated by diets that</li>
    <li><svg width="16" height="16" viewBox="0 0 16 16"><path d="M8 0L9.5 6.5 16 8 9.5 9.5 8 16 6.5 9.5 0 8 6.5 6.5Z" fill="var(--green)"/></svg>If you are frustrated by diets that don’t work</li>
    <li><svg width="16" height="16" viewBox="0 0 16 16"><path d="M8 0L9.5 6.5 16 8 9.5 9.5 8 16 6.5 9.5 0 8 6.5 6.5Z" fill="var(--green)"/></svg>If you are frustrated by diets</li>
    <li><svg width="16" height="16" viewBox="0 0 16 16"><path d="M8 0L9.5 6.5 16 8 9.5 9.5 8 16 6.5 9.5 0 8 6.5 6.5Z" fill="var(--green)"/></svg>If you are frustrated by diets that don’t work</li>
  </ul>
</section>

<section class="review">
  <div class="abs center stars" style="top:88px">★★★★★</div>
  <p class="abs quote">“Before and after is a great place for someone needing to boost there confidence. The staff is friendly and supportive they genuinely care. I have to give a big shout out to Doctor Ravel he is amazing and highly skilled. I do not trust just anyone and he has exceeded my expectations. I have been seeing him for lip injections. I was looking for a change wanted to feel sexier and soften my smile lines.”</p>
  <div class="ph" role="img" aria-label="Handwritten signature of Elowen Marsh" style="left:495px;top:330px;width:210px;height:56px;background:linear-gradient(90deg,rgba(15,163,130,0),rgba(15,163,130,.18),rgba(15,163,130,0))"></div>
</section>

<section class="care">
  <h2 class="abs center h2" style="top:81px">We care about <span class="script">Health</span></h2>
  <p class="abs center lead" style="top:137px;left:210px;width:780px">If you are frustrated by diets that don’t work, we can help. Our medically supervised weight loss plans are designed to help you lose fat and feel healthier. We combine proven medical</p>
  <article class="abs care-card" style="left:123px">
    <div class="ph photo" role="img" aria-label="Gloved hands of a therapist treating a patient's arm" style="background:linear-gradient(135deg,#c9b6a3,#6c6f73 60%,#2a2a2a)"></div>
    <h3>Hormone Replacement <span>TherapyAge</span> Healthier, Live Happier.</h3>
    <p>If you are frustrated by diets that don’t work, we can help. Our medically supervised weight loss plans are designed to help you lose fat and feel healthier.</p>
  </article>
  <article class="abs care-card" style="left:617px">
    <div class="ph photo" role="img" aria-label="Skin care spray bottle beside pink flowers" style="background:linear-gradient(135deg,#e7c4c0,#f1ece8 55%,#d5d2cd)"></div>
    <h3>Skin Care Products Feel Confident in <span>Your Skin</span> and Health</h3>
    <p>If you are frustrated by diets that don’t work, we can help. Our medically supervised weight loss plans are designed to help you lose fat and feel healthier.</p>
  </article>
</section>

<section class="team">
  <h2 class="abs center h2" style="top:43px">Our Expert Team</h2>
  <p class="abs center lead" style="top:100px;left:220px;width:760px">Lorem ipsum dolor sit amet, sit probatus quaerendum sale noluisse partiendo ad, cibo accumsan sit ea. Oratio lucilius ex qui, ex possit similique.</p>
  <div class="abs member" style="left:133px"><div class="avatar" role="img" aria-label="Portrait of doctor Tomas Ridley"></div><h4>Tomas Ridley</h4><span>Orthopedic</span></div>
  <div class="abs member" style="left:370px"><div class="avatar" role="img" aria-label="Portrait of doctor Owen Halvers"></div><h4>Owen Halvers</h4><span>Orthopedic</span></div>
  <div class="abs member" style="left:608px"><div class="avatar" role="img" aria-label="Portrait of doctor Clara Winslet"></div><h4>Clara Winslet</h4><span>Orthopedic</span></div>
  <div class="abs member" style="left:847px"><div class="avatar" role="img" aria-label="Portrait of doctor Dorian Keele"></div><h4>Dorian Keele</h4><span>Orthopedic</span></div>
</section>

<section class="news">
  <h2 class="abs">Subscribe Our Newsletter</h2>
  <p class="abs">Lorem ipsum dolor sit amet, sit probatus quaerendum sale noluisse partiendo ad, cibo accumsan sit ea. Oratio lucilius ex qui, ex possit similique.</p>
  <div class="abs field">Email<div class="sub">Subscribe</div></div>
  <div class="ph" role="img" aria-label="Young woman smiling at her phone" style="left:582px;top:4px;width:290px;height:240px;border-radius:40px;background:radial-gradient(circle at 60% 45%,rgba(255,255,255,.55),rgba(255,255,255,0) 65%)"></div>
</section>

<footer class="footer">
  <div class="abs brand" style="left:243px;top:52px"><span class="brand-dot"></span>Brightfernrx</div>
  <div class="abs foot-links" style="left:243px;top:113px"><div>About Us</div><div>Our Services</div><div>Injection</div><div>Instructions</div></div>
  <div class="btn" style="left:855px;top:53px;width:100px;height:30px;font-size:12px">Get Started</div>
  <div class="abs foot-links" style="right:243px;top:113px;text-align:right"><div>Contact Us</div><div>Return Policy</div><div>Privacy Policy</div><div>Terms and Conditions</div></div>
  <div class="abs rule"></div>
  <div class="abs center" style="top:288px;font-size:12px">Copyright 2022 weight loss All Rights Reserved</div>
</footer>

</body>
</html>
```